5 quadrogram (and fotolume) posts for advertising a service of Online Medicine.
This is NOT a quadrogram page design. This is just quadrogram (and Fotolume) posts design.

We are a medical company providing medicine at distance, using standard videoconsultation and sometimes videoconsultation with a medical device that collects vital signs.

Each post should have:
- Our logo (attached) – if needed it can be just the circular form, but that´s up to you to decide. Ofcourse some design work can be done to this form (watermark, change in dimension, etc)
- Some posts can have the photo of the device (not all the posts because we also provide videoconsultations without the device) – for this please use our website to collect images (https://www.nucleosaudelonge.example/en/pulsora-duo). You can also use the video of the device to collect images (provided as attachment).
- Some stock image at your decision or collected from our website (https://www.nucleosaudelonge.example/pt/medicina-online) or from the provided video (all of these are licensed and you can use them freely – for instance you can collect doctors from our video)
- One or more of the following headlines (please use different headlines for different posts):
 Revolução na Qualidade da Videoconsulta
 O seu Médico com acesso à informação da sua Brisa Corpo
 Sincronização com Brisa Corpo
 Possibilidade de usar o dispositivo PulsoraDuo | Medição à Distância de 6 Sinais Vitais
 Revolução na Saúde
 Revolução na Medicina à Distância
 Um Novo Mundo na Saúde
 Segurança e Fiabilidade na Medicina à Distância
 Excelência na Medicina à Distância
 Baixa Médica Online
 Atestados de Saúde
 Renovação de Receituário
 Planos de Monitorização Remota e Acompanhamento Médico desde 10 EUR / Mês

We need 5 posts, all different between each other but where we can feel an aesthetical and graphic/design continuity/coherence of course.
Each post should be provided on adequate format for quadrogram and Fotolume publishing.

Target Market(s)

Patients

Industry/Entity Type

Medicine

Requirements
Must have
• Check description
Nice to have
• Check description

```html
<!DOCTYPE html>
<html lang="pt">
<head>
<meta charset="utf-8">
<title>Núcleo Saúde Longe – Revolução na Qualidade da Videoconsulta</title>
<link rel="stylesheet" href="https://fonts.googleapis.com/css2?family=Outfit:wght@300;400;500;600&display=swap">
<style>
  :root {
    --blue-deep: #0e6a94;
    --blue-head: #12709b;
    --blue-logo: #1b86ba;
    --ink: #363a3e;
    --ink-soft: #5b6166;
    --white: #ffffff;
    --photo-wall: #b7c9d8;
    --photo-shirt: #cfdceb;
    --photo-warm: #d9cfc8;
    --photo-light: #eef3f7;
    --device-rim: #e4e7ea;
    --device-body: #3a3f46;
    --device-screen: #1f2328;
  }
  html, body {
    margin: 0;
    padding: 0;
    width: 1200px;
    height: 1200px;
    overflow: hidden;
    background: var(--white);
  }
  .post {
    position: relative;
    width: 1200px;
    height: 1200px;
    overflow: hidden;
    background: var(--white);
    font-family: "Outfit", sans-serif;
  }
  .hero-photo {
    position: absolute;
    left: 0;
    top: 0;
    width: 640px;
    height: 640px;
    background:
      linear-gradient(to right, rgba(255,255,255,0) 55%, var(--white) 100%),
      linear-gradient(to bottom, rgba(255,255,255,0) 50%, var(--white) 100%),
      linear-gradient(150deg, var(--photo-warm) 0%, var(--photo-wall) 30%, var(--photo-shirt) 60%, var(--photo-light) 100%);
  }
  .brand {
    position: absolute;
    left: 652px;
    top: 124px;
    display: flex;
    align-items: center;
    gap: 18px;
  }
  .brand-mark {
    width: 88px;
    height: 88px;
    background: var(--blue-logo);
    border-radius: 6px;
  }
  .brand-name {
    margin: 0;
    font-size: 44px;
    line-height: 0.95;
    font-weight: 600;
    color: var(--blue-logo);
    letter-spacing: 0.5px;
  }
  .brand-owner {
    margin: 6px 0 0;
    font-size: 20px;
    font-weight: 400;
    color: var(--ink-soft);
  }
  .vitals-panel {
    position: absolute;
    left: 850px;
    top: 329px;
    width: 350px;
    height: 822px;
    background: var(--blue-deep);
    border-radius: 42px 0 0 42px;
  }
  .device {
    position: absolute;
    left: 556px;
    top: 374px;
    width: 500px;
    height: 316px;
    border-radius: 158px;
    background: linear-gradient(135deg, var(--device-rim) 0%, var(--device-body) 35%, var(--device-screen) 65%, var(--device-body) 100%);
    box-shadow: 0 20px 44px rgba(0,0,0,0.22);
  }
  .headline {
    position: absolute;
    left: 86px;
    top: 614px;
    margin: 0;
    font-size: 90px;
    line-height: 108px;
    font-weight: 500;
    color: var(--ink);
    letter-spacing: -0.5px;
  }
  .headline .accent { color: var(--blue-head); }
  .vitals-list {
    position: absolute;
    left: 878px;
    top: 748px;
    margin: 0;
    padding: 0;
    list-style: none;
  }
  .vitals-list li {
    display: flex;
    align-items: center;
    gap: 12px;
    height: 36px;
    font-size: 17px;
    color: var(--white);
  }
  .vitals-list svg { width: 20px; height: 20px; flex: none; }
  .panel-rule {
    position: absolute;
    left: 878px;
    top: 988px;
    width: 256px;
    height: 1px;
    background: rgba(255,255,255,0.5);
  }
  .service {
    position: absolute;
    left: 878px;
    top: 1016px;
    display: flex;
    align-items: center;
    gap: 8px;
    color: var(--white);
  }
  .service-label {
    writing-mode: vertical-rl;
    transform: rotate(180deg);
    font-size: 22px;
    font-weight: 400;
  }
  .service-hours {
    font-size: 106px;
    line-height: 1;
    font-weight: 300;
  }
  .footer-tab {
    position: absolute;
    left: 0;
    top: 1107px;
    width: 56px;
    height: 38px;
    background: var(--blue-logo);
  }
  .site-url {
    position: absolute;
    left: 100px;
    top: 1104px;
    margin: 0;
    font-size: 33px;
    font-weight: 400;
    color: var(--ink);
  }
</style>
</head>
<body>
<main class="post">
  <div class="hero-photo" role="img" aria-label="Médico com auscultadores e estetoscópio durante uma videoconsulta"></div>

  <header class="brand">
    <div class="brand-mark"></div>
    <div>
      <p class="brand-name">NÚCLEO SAÚDE<br>LONGE</p>
      <p class="brand-owner">Professora Doutora Inês Calado</p>
    </div>
  </header>

  <section class="vitals-panel"></section>

  <div class="device" role="img" aria-label="Dispositivo PulsoraDuo de medição de sinais vitais com ecrã tátil e sensores de ECG"></div>

  <h1 class="headline">
    <span class="accent">Revolução</span><br>
    na Qualidade da<br>
    <span class="accent">Videoconsulta</span>
  </h1>

  <ul class="vitals-list">
    <li><svg viewBox="0 0 20 20"><circle cx="10" cy="10" r="8.5" fill="none" stroke="#fff" stroke-width="1.5"/><path d="M6 10.2l2.7 2.6L14 7.5" fill="none" stroke="#fff" stroke-width="1.6" stroke-linecap="round" stroke-linejoin="round"/></svg>Frequência Cardíaca</li>
    <li><svg viewBox="0 0 20 20"><circle cx="10" cy="10" r="8.5" fill="none" stroke="#fff" stroke-width="1.5"/><path d="M6 10.2l2.7 2.6L14 7.5" fill="none" stroke="#fff" stroke-width="1.6" stroke-linecap="round" stroke-linejoin="round"/></svg>Pressão Arteria</li>
    <li><svg viewBox="0 0 20 20"><circle cx="10" cy="10" r="8.5" fill="none" stroke="#fff" stroke-width="1.5"/><path d="M6 10.2l2.7 2.6L14 7.5" fill="none" stroke="#fff" stroke-width="1.6" stroke-linecap="round" stroke-linejoin="round"/></svg>Níveis de Oxigénio no Sangue</li>
    <li><svg viewBox="0 0 20 20"><circle cx="10" cy="10" r="8.5" fill="none" stroke="#fff" stroke-width="1.5"/><path d="M6 10.2l2.7 2.6L14 7.5" fill="none" stroke="#fff" stroke-width="1.6" stroke-linecap="round" stroke-linejoin="round"/></svg>Temperatura Corporal</li>
    <li><svg viewBox="0 0 20 20"><circle cx="10" cy="10" r="8.5" fill="none" stroke="#fff" stroke-width="1.5"/><path d="M6 10.2l2.7 2.6L14 7.5" fill="none" stroke="#fff" stroke-width="1.6" stroke-linecap="round" stroke-linejoin="round"/></svg>Eletrocardiograma</li>
    <li><svg viewBox="0 0 20 20"><circle cx="10" cy="10" r="8.5" fill="none" stroke="#fff" stroke-width="1.5"/><path d="M6 10.2l2.7 2.6L14 7.5" fill="none" stroke="#fff" stroke-width="1.6" stroke-linecap="round" stroke-linejoin="round"/></svg>Açúcar no Sangue</li>
  </ul>

  <div class="panel-rule"></div>

  <div class="service">
    <span class="service-label">Serviço</span>
    <span class="service-hours">24/7</span>
  </div>

  <div class="footer-tab"></div>
  <p class="site-url">www.nucleosaudelonge.example</p>
</main>
</body>
</html>
```